RW Skyline Imaging Web Site design

I am looking for a responsive single page website deign for rwskylineimages.example. This is a drone based aerial photography and cinematography business. It should have an about us section, a services section that contains photograph service, Video footage, and Aerial mapping all under the services section, a pricing section, and then a contact page for customers to contact us.

Coding

Coded - Design and coding required

Number of Pages Required

1 page

Font styles to use
Sans Serif

Colors

Designer to choose colors to be used in the design.

Requirements
Must have
• Responsive design. About us section, services section, pricing section under the services links, and contact us section, that links to a submission page where they can send Name, address, email, and comments on what they are interested in.
• See flyquad7x.example - looking for similar design.
Should not have
• clutter, or too busy design

```html
<!DOCTYPE html>
<html lang="en">
<head>
<meta charset="utf-8">
<title>RW Skyline Imaging — Welcome</title>
<link rel="stylesheet" href="https://fonts.googleapis.com/css2?family=Oswald:wght@400;500;600;700&display=swap">
<style>
:root{
  --navy:#0f3a52;
  --red:#e8192c;
  --ink:#333333;
  --grey:#a9a9a9;
  --bg:#ffffff;
}
*{margin:0;padding:0;box-sizing:border-box}
html,body{width:1126px;height:1200px;overflow:hidden;background:var(--bg)}
body{position:relative;font-family:"Oswald",sans-serif;text-transform:uppercase;color:var(--ink)}
.abs{position:absolute}
.top-btn{left:117px;top:38px;width:29px;height:29px}
.welcome-title{left:186px;top:30px;font-size:31px;font-weight:700;color:var(--navy);letter-spacing:.3px;line-height:40px}
.title-dots{left:211px;top:65px;width:86px;height:10px}
.intro{left:187px;top:84px;width:940px;font-size:17px;font-weight:500;line-height:22.5px;letter-spacing:.2px}
.intro--accent{top:151px;color:var(--red)}
.showreel{left:184px;top:219px;width:778px;height:439px;background:linear-gradient(160deg,#4d5750 0%,#3b3e3c 45%,#2f3340 100%);box-shadow:0 8px 22px rgba(0,0,0,.45)}
.showreel .play{position:absolute;left:333px;top:180px;width:114px;height:80px}
.section-title{font-size:17px;font-weight:600;color:var(--red);letter-spacing:.3px;line-height:22px}
.services-title{left:186px;top:694px}
.services-text{left:186px;top:727px;width:780px;font-size:17px;font-weight:500;line-height:22.4px;letter-spacing:.2px}
.col-a{left:186px}
.col-b{left:563px}
.service-heading{top:809px}
.service-media{top:840px;width:311px;height:221px}
.service-media--photo{background:linear-gradient(160deg,#c9565f 0%,#b23c4a 55%,#8f2c3a 100%)}
.service-media--video{background:linear-gradient(160deg,#5a5548 0%,#3a3530 40%,#5d6a4c 75%,#3a2f2e 100%)}
.service-media .icon{position:absolute;left:103px;top:58px;width:105px;height:105px}
.service-caption{top:1075px;width:330px;font-size:17px;font-weight:500;line-height:22.4px;letter-spacing:.2px}
.mapping-heading{top:1140px}
.mapping-media{top:1171px;width:311px;height:40px}
.mapping-media--a{background:linear-gradient(180deg,#4e6a3c,#6b7f55)}
.mapping-media--b{background:linear-gradient(180deg,#e6ebe0,#a9b98e)}
</style>
</head>
<body>

<svg class="abs top-btn" viewBox="0 0 29 29" aria-label="Back to top">
  <circle cx="14.5" cy="14.5" r="14.5" fill="var(--grey)"/>
  <path d="M8 17.5 L14.5 10.5 L21 17.5" fill="none" stroke="#fff" stroke-width="3.4" stroke-linecap="round" stroke-linejoin="round"/>
</svg>

<h1 class="abs welcome-title">Welcome</h1>
<svg class="abs title-dots" viewBox="0 0 86 10">
  <g fill="none" stroke="var(--red)" stroke-width="1.8">
    <circle cx="5" cy="5" r="3.6"/><circle cx="24" cy="5" r="3.6"/><circle cx="43" cy="5" r="3.6"/><circle cx="62" cy="5" r="3.6"/><circle cx="81" cy="5" r="3.6"/>
  </g>
</svg>

<p class="abs intro">If your'e looking for professional photography or videography you've come to the no matter what you needs I can help in the past I have worked with a range of business and indurtries such a</p>
<p class="abs intro intro--accent">For a wide varity of events function and tasks find my to be s real estate constructions and media companiesright place as I capture stunning arial</p>

<div class="abs showreel" role="img" aria-label="Showreel video still: a group of friends taking a selfie outdoors">
  <svg class="play" viewBox="0 0 114 80">
    <g fill="none" stroke="#fff" stroke-width="6" stroke-linecap="round">
      <path d="M22 12 A40 40 0 0 0 22 68"/><path d="M10 4 A52 52 0 0 0 10 76"/>
      <path d="M92 12 A40 40 0 0 1 92 68"/><path d="M104 4 A52 52 0 0 1 104 76"/>
    </g>
    <circle cx="57" cy="40" r="27" fill="#fff"/>
    <path d="M50 28 L69 40 L50 52 Z" fill="#111"/>
  </svg>
</div>

<h2 class="abs section-title services-title">Drone Aerial - Photo &amp; Video Services</h2>
<p class="abs services-text">As a fully licensed operator . I can provide you with all of the services you need I only use high quilty and pretty awesome technology so you know you will receive exceptional images and video you find me easy to work with and I always like to special</p>

<h3 class="abs section-title service-heading col-a">Photography</h3>
<h3 class="abs section-title service-heading col-b">Videography</h3>

<div class="abs service-media service-media--photo col-a" role="img" aria-label="Photography service: group selfie with red overlay">
  <svg class="icon" viewBox="0 0 105 105">
    <circle cx="52.5" cy="52.5" r="51" fill="none" stroke="rgba(255,255,255,.8)" stroke-width="2"/>
    <g fill="none" stroke="rgba(255,255,255,.8)" stroke-width="3" stroke-linejoin="round">
      <rect x="28" y="36" width="49" height="34" rx="4"/>
      <path d="M40 36 L44 29 H61 L65 36"/>
      <circle cx="52.5" cy="53" r="10"/><circle cx="52.5" cy="53" r="4"/>
      <line x1="68" y1="44" x2="72" y2="44"/>
    </g>
  </svg>
</div>

<div class="abs service-media service-media--video col-b" role="img" aria-label="Videography service: grid of wedding film stills">
  <svg class="icon" viewBox="0 0 105 105">
    <circle cx="52.5" cy="52.5" r="51" fill="rgba(0,0,0,.25)" stroke="rgba(255,255,255,.8)" stroke-width="2"/>
    <g fill="none" stroke="rgba(255,255,255,.85)" stroke-width="3" stroke-linejoin="round">
      <rect x="18" y="38" width="52" height="30" rx="8"/>
      <path d="M70 50 L87 38 V68 L70 56"/>
    </g>
  </svg>
</div>

<p class="abs service-caption col-a">Drone photography services includs editing titing and more</p>
<p class="abs service-caption col-b">Available drone videopraghy services includs filming, editing, music, litling</p>

<h3 class="abs section-title mapping-heading col-a">3D Mapping</h3>
<h3 class="abs section-title mapping-heading col-b">3D Mapping</h3>

<div class="abs mapping-media mapping-media--a col-a" role="img" aria-label="3D mapping render of a wooded site"></div>
<div class="abs mapping-media mapping-media--b col-b" role="img" aria-label="Aerial mapping view of open countryside"></div>

</body>
</html>
```